Designs of screens for job search mobile app

Design the following screens:

1. Login
2. Job search results in tabs
3. Job details in cards format
4. Profile
5. Settings

Logo and references are provided. The app need to be playful, easy to use, different from traditional job search app like Workvane, ProLattice and others and targeted to Millennial users (age 18-30).

The main app reference is Piqto, in terms of the colorful and fun color and font scheme.

Target Market(s)

Millennial users (age 18-30).

Requirements
Must have
• A fun, playful feel

```html
<!DOCTYPE html>
<html lang="en">
<head>
<meta charset="utf-8">
<title>JobRover – Log In</title>
<link href="https://fonts.googleapis.com/css2?family=Figtree:wght@400;500;600;700&display=swap" rel="stylesheet">
<style>
  :root {
    --canvas-bg: #f6f5f5;
    --screen-bg: #ffffff;
    --teal: #00bdb9;
    --ink: #2b2b2b;
    --ink-soft: #4a4a4a;
    --muted: #b9b9b9;
    --rule: #e6e6e6;
    --social-blue: #3d5a9b;
    --white: #ffffff;
  }
  * { box-sizing: border-box; margin: 0; padding: 0; }
  html, body {
    width: 1200px; height: 1200px; overflow: hidden;
    background: var(--canvas-bg);
    font-family: "Figtree", "Helvetica Neue", Arial, sans-serif;
    color: var(--ink);
  }
  .login-screen {
    position: absolute; left: 284px; top: 38px;
    width: 632px; height: 1124px;
    background: var(--screen-bg);
    box-shadow: 0 10px 40px rgba(0,0,0,0.06);
  }
  .status-bar {
    position: absolute; left: 0; top: 0; width: 100%; height: 48px;
    display: flex; align-items: center; justify-content: space-between;
    padding: 0 16px; font-size: 19px; font-weight: 500; color: var(--ink);
  }
  .status-left, .status-right { display: flex; align-items: center; gap: 8px; width: 200px; }
  .status-right { justify-content: flex-end; }
  .status-time { font-weight: 600; }
  .nav-title {
    position: absolute; left: 0; top: 48px; width: 100%; height: 54px;
    text-align: center; line-height: 44px;
    font-size: 24px; font-weight: 700; color: var(--ink);
  }
  .nav-rule {
    position: absolute; left: 24px; right: 24px; top: 102px;
    height: 2px; background: var(--rule);
  }
  .brand { position: absolute; left: 0; top: 180px; width: 100%; text-align: center; }
  .brand-dot {
    display: block; margin: 0 auto;
    width: 104px; height: 104px; border-radius: 50%;
    background: var(--teal);
  }
  .brand-name {
    display: block; margin-top: 14px;
    font-size: 46px; font-weight: 500; color: var(--ink-soft); letter-spacing: -0.5px;
  }
  .field {
    position: absolute; left: 88px; width: 448px; height: 64px;
    display: flex; align-items: center; gap: 18px; padding-left: 4px;
    border-bottom: 2px solid var(--rule);
    color: var(--teal); font-size: 22px; font-weight: 600;
  }
  .field-email { top: 442px; }
  .field-password { top: 516px; }
  .password-dots { letter-spacing: 6px; font-size: 30px; line-height: 1; }
  .forgot {
    position: absolute; left: 92px; top: 600px;
    font-size: 17px; font-weight: 500; color: var(--ink);
  }
  .forgot a, .footer a { color: var(--ink); font-weight: 700; text-decoration: none; border-bottom: 1px solid var(--ink); }
  .btn {
    position: absolute; left: 84px; width: 460px; height: 66px;
    border-radius: 33px; border: none;
    display: flex; align-items: center; justify-content: center;
    font-family: inherit; font-size: 27px; font-weight: 500; color: var(--white);
  }
  .btn-login { top: 674px; background: var(--teal); }
  .btn-social { top: 802px; background: var(--social-blue); }
  .divider {
    position: absolute; left: 88px; width: 448px; top: 760px;
    display: flex; align-items: center; gap: 18px;
    font-size: 17px; color: var(--muted); letter-spacing: 1px;
  }
  .divider::before, .divider::after { content: ""; flex: 1; height: 2px; background: var(--rule); }
  .footer {
    position: absolute; left: 0; top: 1072px; width: 100%; text-align: center;
    font-size: 20px; font-weight: 500; color: var(--ink);
  }
</style>
</head>
<body>
  <main class="login-screen">
    <div class="status-bar">
      <div class="status-left">
        <svg width="50" height="10" viewBox="0 0 50 10" aria-hidden="true">
          <circle cx="5" cy="5" r="4" fill="#2b2b2b"/><circle cx="15" cy="5" r="4" fill="#2b2b2b"/><circle cx="25" cy="5" r="4" fill="#2b2b2b"/>
          <circle cx="35" cy="5" r="3.4" fill="none" stroke="#2b2b2b" stroke-width="1.2"/><circle cx="45" cy="5" r="3.4" fill="none" stroke="#2b2b2b" stroke-width="1.2"/>
        </svg>
        <span>NOVA</span>
        <svg width="20" height="15" viewBox="0 0 20 15" aria-hidden="true">
          <path d="M1 5a13 13 0 0 1 18 0M4 8.5a8.5 8.5 0 0 1 12 0M7 11.5a4 4 0 0 1 6 0" fill="none" stroke="#2b2b2b" stroke-width="2" stroke-linecap="round"/>
          <circle cx="10" cy="14" r="1.2" fill="#2b2b2b"/>
        </svg>
      </div>
      <span class="status-time">4:21 PM</span>
      <div class="status-right">
        <svg width="10" height="16" viewBox="0 0 10 16" aria-hidden="true">
          <path d="M1 4.5l8 7-4 3.5V1l4 3.5-8 7" fill="none" stroke="#8a8a8a" stroke-width="1.5"/>
        </svg>
        <span>100%</span>
        <svg width="40" height="16" viewBox="0 0 40 16" aria-hidden="true">
          <rect x="1" y="1" width="34" height="14" rx="3" fill="none" stroke="#2b2b2b" stroke-width="1.5"/>
          <rect x="3" y="3" width="30" height="10" rx="1.5" fill="#2b2b2b"/>
          <rect x="36.5" y="5" width="2.5" height="6" rx="1" fill="#2b2b2b"/>
        </svg>
      </div>
    </div>

    <h1 class="nav-title">Log In</h1>
    <div class="nav-rule"></div>

    <div class="brand">
      <span class="brand-dot"></span>
      <span class="brand-name">JobRover</span>
    </div>

    <div class="field field-email">
      <svg width="34" height="34" viewBox="0 0 34 34" aria-hidden="true">
        <circle cx="17" cy="12" r="7" fill="none" stroke="#00bdb9" stroke-width="2.2"/>
        <path d="M3 31c1-8 7-11 14-11s13 3 14 11z" fill="none" stroke="#00bdb9" stroke-width="2.2" stroke-linejoin="round"/>
      </svg>
      <span>yourname@email.com</span>
    </div>

    <div class="field field-password">
      <svg width="34" height="36" viewBox="0 0 34 36" aria-hidden="true">
        <path d="M10 15v-5a7 7 0 0 1 14 0v5" fill="none" stroke="#00bdb9" stroke-width="2.2"/>
        <circle cx="17" cy="24" r="10" fill="none" stroke="#00bdb9" stroke-width="2.2"/>
        <circle cx="17" cy="22.5" r="2.2" fill="#00bdb9"/>
        <path d="M17 24v4" stroke="#00bdb9" stroke-width="2.2" stroke-linecap="round"/>
      </svg>
      <span class="password-dots">●●●●●</span>
    </div>

    <p class="forgot">Forgot Password? <a href="#">Click Here</a></p>

    <button class="btn btn-login" type="button">Log In</button>
    <div class="divider">OR</div>
    <button class="btn btn-social" type="button">Sign In With Circlo</button>

    <p class="footer">Don't Have a Account? <a href="#">Sign Up</a></p>
  </main>
</body>
</html>
```